NPG Job bank

Western Guild of Bracework Practitioners Needs a design for our orthodontist job bank.

We are in the process of redesigning our current job board. We would like to improve our current design, focusing on the landing page and possibly the search page. I have attached images of what we currently have in place right now.

The Landing page: Currently, I find the landing page too wordy, members get confused when using it, we need something that is easier for providers are seekers to use. Set up more user friendly. Maybe have a button for become provider and become seeker and then a modal pops up with process.. The final design for this page needs to be user friendly, organized and clean. If someone were coming to this page for the first time they would know how to become a provider.

The search page: I was thinking it would be best to have the search options on the left hand side opposed to how it is just in the middle now. all of the information currently shown on this page needs to be included. The search results need improvement on how they are displayed as well.

If you have any questions feel free to contact me.

Industry/Entity Type

Bank

Number of Pages Required

1 page

Colors
33a6d7
85cae6
0692cd

Requirements
Must have
• A Landing page that is well designed and that is made in the blue colors that are shown on the attached files of what our job bank currently looks like. I have also attached 3 photos that could be used for a masthead, but keep in mind these do not have to be used, you can use any photo you would like, these are just for your convenience.
Nice to have
• An improved search results page along with the Landing page

```html
<!DOCTYPE html>
<html lang="en">
<head>
<meta charset="utf-8">
<title>NPG Job Bank</title>
<link rel="stylesheet" href="https://fonts.googleapis.com/css2?family=Source+Sans+3:wght@300;400;600&display=swap">
<style>
:root{
  --blue-deep:#0692cd;
  --blue-mid:#33a6d7;
  --blue-light:#85cae6;
  --nav-top:#1aa3dc;
  --nav-bottom:#0a8fcb;
  --brand-ink:#1f5aa6;
  --ink:#4a4a4a;
  --ink-soft:#6b6b6b;
  --title-warm:#5a3b2e;
  --footer-bg:#222222;
  --white:#ffffff;
}
*{box-sizing:border-box;margin:0;padding:0}
html,body{width:1200px;height:2314px;overflow:hidden;background:var(--white)}
body{font-family:"Source Sans 3",Arial,sans-serif;color:var(--ink);position:relative}

.site-header{position:absolute;left:0;top:0;width:1200px;height:223px}
.brand{position:absolute;left:86px;top:68px;display:flex;align-items:flex-start;gap:18px}
.brand-square{width:142px;height:117px;background:var(--blue-deep);border-radius:8px}
.brand-text{color:var(--brand-ink);font-weight:400;line-height:1.0;padding-top:2px}
.brand-text .member{font-size:22px;display:block;margin-bottom:4px}
.brand-text .name{font-size:31px;display:block;width:240px;line-height:30px}
.account-links{position:absolute;right:86px;top:88px;font-size:18px;color:#7a7a7a;letter-spacing:.5px}
.search-box{position:absolute;left:853px;top:136px;width:261px;height:36px;border:1px solid #cfcfcf;display:flex;align-items:center;padding:0 12px;font-size:14px;color:#8a8a8a;justify-content:space-between}

.main-nav{position:absolute;left:0;top:223px;width:1200px;height:59px;background:linear-gradient(var(--nav-top),var(--nav-bottom))}
.main-nav ul{list-style:none;position:absolute;left:86px;top:0;height:59px;display:flex}
.main-nav li{height:59px;display:flex;align-items:center;justify-content:center;color:var(--white);font-size:18px;border-right:1px solid rgba(255,255,255,.25)}
.main-nav li.active{background:var(--blue-light)}

.hero{position:absolute;left:0;top:282px;width:1200px;height:571px;background:linear-gradient(100deg,#8fc2e2 0%,#6eaed6 40%,#d9c2b2 62%,#f2efec 75%,#5f9fcc 100%)}
.hero-arrow{position:absolute;top:481px;width:61px;height:61px;border-radius:50%;background:rgba(40,60,80,.45)}
.hero-arrow.prev{left:86px}.hero-arrow.next{left:1053px}
.hero-arrow svg{display:block}

.welcome{position:absolute;left:0;top:915px;width:1200px;text-align:center}
.welcome h1{font-weight:400;font-size:35px;color:var(--title-warm)}
.welcome h1 span{color:var(--brand-ink)}
.welcome p{width:1010px;margin:22px auto 0;font-size:14px;line-height:26px;color:var(--ink-soft)}

.paths{position:absolute;left:0;top:1128px;width:1200px;height:742px;display:flex}
.path{height:742px;color:var(--white);text-align:center;position:relative}
.path.provider{width:598px;background:var(--blue-deep)}
.path.seeker{width:602px;background:var(--blue-mid)}
.path h2{position:absolute;top:66px;width:100%;font-weight:400;font-size:43px;letter-spacing:.5px}
.path .lead{position:absolute;top:140px;width:100%;font-size:23px}
.path .rule{position:absolute;top:194px;left:155px;width:290px;height:1px;background:rgba(255,255,255,.25)}
.steps{position:absolute;top:222px;width:100%;list-style:none}
.steps li{font-size:22px;height:32px;line-height:32px}
.steps .chev{height:50px;display:flex;align-items:center;justify-content:center}
.btn-outline{position:absolute;top:629px;left:50%;transform:translateX(-50%);width:252px;height:50px;border:2px solid var(--white);font-size:22px;line-height:46px}

.newsletter{position:absolute;left:0;top:1870px;width:1200px;height:188px}
.newsletter h3{position:absolute;left:117px;top:58px;font-weight:300;font-size:43px;color:#555}
.newsletter .field{position:absolute;left:596px;top:66px;width:336px;height:50px;border:1px solid #9a9a9a;font-size:14px;line-height:48px;padding-left:14px;color:#555}
.newsletter .signup{position:absolute;left:932px;top:66px;width:155px;height:50px;background:var(--blue-deep);color:var(--white);font-size:24px;line-height:50px;text-align:center}

.site-footer{position:absolute;left:0;top:2058px;width:1200px;height:256px;background:var(--footer-bg);color:var(--white);text-align:center;font-family:Arial,Helvetica,sans-serif}
.social{position:absolute;top:48px;left:476px;display:flex;gap:17px}
.social span{width:61px;height:61px;border:2px solid #9a9a9a;border-radius:50%}
.footer-links{position:absolute;top:156px;width:100%;font-size:14px}
.copyright{position:absolute;top:191px;width:100%;font-size:14px}
</style>
</head>
<body>
<header class="site-header">
  <div class="brand">
    <div class="brand-square"></div>
    <div class="brand-text"><span class="member">NPG Member</span><span class="name">Western Guild of Bracework Practitioners</span></div>
  </div>
  <div class="account-links">JOIN | SIGN IN</div>
  <div class="search-box"><span>Search..</span>
    <svg width="14" height="14" viewBox="0 0 14 14"><circle cx="6" cy="6" r="4.5" fill="none" stroke="#999" stroke-width="1.6"/><line x1="9.3" y1="9.3" x2="13" y2="13" stroke="#999" stroke-width="1.8"/></svg>
  </div>
</header>

<nav class="main-nav">
  <ul>
    <li class="active" style="width:212px">MEETINGS &amp; EVENTS</li>
    <li style="width:144px">EDUCATION</li>
    <li style="width:242px">PRACTICE MANAGEMENT</li>
    <li style="width:164px">PUBLICATIONS</li>
    <li style="width:97px">LEGAL</li>
    <li style="width:158px;border-right:0">COMMUNITIES</li>
  </ul>
</nav>

<section class="hero" role="img" aria-label="Masthead photo: a smiling woman with raised arms against a blue sea and sky">
  <div class="hero-arrow prev"><svg width="61" height="61" viewBox="0 0 61 61"><polyline points="34,20 24,30.5 34,41" fill="none" stroke="#fff" stroke-width="2"/></svg></div>
  <div class="hero-arrow next"><svg width="61" height="61" viewBox="0 0 61 61"><polyline points="27,20 37,30.5 27,41" fill="none" stroke="#fff" stroke-width="2"/></svg></div>
</section>

<section class="welcome">
  <h1>Welcome To <span>Our Website</span></h1>
  <p>Typi non habent claritatem insitam; est usus legentis in iis qui facit eorum claritatem. Investigationes demonstraverunt lectores legere me lius quod ii legunt saepius. Claritas est etiam processus dynamicus, qui sequitur mutationem consuetudium lectorum. Mirum est notare quam littera gothica, quam nunc putamus parum claram, anteposuerit litterarum formas humanitatis per seacula quarta decima et quinta decima. Eodem modo typi, qui nunc nobis videntur parum clari, fiant sollemnes in futurum.</p>
</section>

<section class="paths">
  <div class="path provider">
    <h2>PROVIDER</h2>
    <div class="lead">Post an Oppurtunity or Search Resumes</div>
    <div class="rule"></div>
    <ul class="steps">
      <li>Request Access</li>
      <li class="chev"><svg width="22" height="16" viewBox="0 0 22 16"><polyline points="3,2 11,8 19,2" fill="none" stroke="#fff" stroke-width="2"/><polyline points="3,8 11,14 19,8" fill="none" stroke="#fff" stroke-width="2"/></svg></li>
      <li>Post Oppurtunity</li>
      <li class="chev"><svg width="22" height="16" viewBox="0 0 22 16"><polyline points="3,2 11,8 19,2" fill="none" stroke="#fff" stroke-width="2"/><polyline points="3,8 11,14 19,8" fill="none" stroke="#fff" stroke-width="2"/></svg></li>
      <li>Search the Resume Center</li>
      <li class="chev"><svg width="22" height="16" viewBox="0 0 22 16"><polyline points="3,2 11,8 19,2" fill="none" stroke="#fff" stroke-width="2"/><polyline points="3,8 11,14 19,8" fill="none" stroke="#fff" stroke-width="2"/></svg></li>
      <li>Access Your Oppurtunities</li>
      <li class="chev"><svg width="22" height="16" viewBox="0 0 22 16"><polyline points="3,2 11,8 19,2" fill="none" stroke="#fff" stroke-width="2"/><polyline points="3,8 11,14 19,8" fill="none" stroke="#fff" stroke-width="2"/></svg></li>
      <li>Frequently Asked Questions</li>
    </ul>
    <div class="btn-outline">BECOME PROVIDER</div>
  </div>
  <div class="path seeker">
    <h2>SEEKER</h2>
    <div class="lead">Post an Oppurtunity or Search Resumes</div>
    <div class="rule"></div>
    <ul class="steps">
      <li>Request Access</li>
      <li class="chev"><svg width="22" height="16" viewBox="0 0 22 16"><polyline points="3,2 11,8 19,2" fill="none" stroke="#fff" stroke-width="2"/><polyline points="3,8 11,14 19,8" fill="none" stroke="#fff" stroke-width="2"/></svg></li>
      <li>Post Oppurtunity</li>
      <li class="chev"><svg width="22" height="16" viewBox="0 0 22 16"><polyline points="3,2 11,8 19,2" fill="none" stroke="#fff" stroke-width="2"/><polyline points="3,8 11,14 19,8" fill="none" stroke="#fff" stroke-width="2"/></svg></li>
      <li>Search the Resume Center</li>
      <li class="chev"><svg width="22" height="16" viewBox="0 0 22 16"><polyline points="3,2 11,8 19,2" fill="none" stroke="#fff" stroke-width="2"/><polyline points="3,8 11,14 19,8" fill="none" stroke="#fff" stroke-width="2"/></svg></li>
      <li>Access Your Oppurtunities</li>
      <li class="chev"><svg width="22" height="16" viewBox="0 0 22 16"><polyline points="3,2 11,8 19,2" fill="none" stroke="#fff" stroke-width="2"/><polyline points="3,8 11,14 19,8" fill="none" stroke="#fff" stroke-width="2"/></svg></li>
      <li>Frequently Asked Questions</li>
    </ul>
    <div class="btn-outline">BECOME SEEKER</div>
  </div>
</section>

<section class="newsletter">
  <h3>Signup for Newsletter</h3>
  <div class="field">Enter the Email Id</div>
  <div class="signup">SIGNUP</div>
</section>

<footer class="site-footer">
  <div class="social" aria-label="Social links"><span></span><span></span><span></span><span></span></div>
  <div class="footer-links">Home &nbsp;|&nbsp; Explore &nbsp;|&nbsp; NPG Member Directory &nbsp;|&nbsp; About &nbsp;|&nbsp; Contact</div>
  <div class="copyright">Copyright © 2013. All Rights Reserved.</div>
</footer>
</body>
</html>
```